Bright Canyon, LLC Business Card Design

We need a product business card designed for a new company Bright Canyon, LLC. We make and resell waterless RV cleaner, polish and protectant. It cleans and protects in a simple spray and wipe step leaving the surface protected and conditioned to repel dust, dirt, water, smudges, bugs and fingerprints while preventing fogging. Safe on acrylic, clarisheet, durvane, plastic, rubber, painted surfaces, chrome, stainless, aluminum, vinyl, leather, glass.... This is an eco-friendly green product.

We want to play off the company name to tell the consumer that the product is easy to use and associate to the nostalgics 1950's in the USA... Thinking old travel trailer with hot rod truck pulling it as the graphic, maybe the husband cleaning the truck and the wife cleaning the trailer for a Bright Canyon surface.
Updates

Just posted our newly finished logo. Need to have "Cleaner and Protectant" added to the design as well. Thanks everyone that has submitted thus far, i am working to get comments on all.

If you need a different file format, please let me know. Thank you.

Most important info, is the logo, website and the words "Cleaner" or "Clean" along "Protectant" or "Protect" the remainder is of less importance. Highlight: www.brightcanyoncleaner.example Focus is on company brand for Brighter Canyon Cleaner product: However, need a section for the following contact info: John Doe (xxx) xxx-xxxx email address Would like space for QR Code if possible.

Target Market(s)

Adults in the USA between ages of 35-75 that are actively involved in the Recreational Vehicle (RV), travel trailer, and hot rod lifestyle. We are targeting the RV marked of the high end travel, 5th wheel and bus RV market. Along with hot rods, automotive and motorcycle market.

Industry/Entity Type

Travel

Requirements
Must have
• Most important info, is the logo, website and the words "Cleaner" or "Clean" along "Protectant" or "Protect" the remainder is of less importance.

Highlight:
www.brightcanyoncleaner.example

Focus is on company brand for Brighter Canyon Cleaner product: However, need a section for the following contact info:

John Doe
(xxx) xxx-xxxx
email address
Nice to have
• Would like a space for a QR Code.

```html
<!DOCTYPE html>
<html lang="en">
<head>
<meta charset="utf-8">
<title>Bright Canyon, LLC – Business Card</title>
<link rel="stylesheet" href="https://fonts.googleapis.com/css2?family=Jost:wght@300;400&display=swap">
<style>
  :root {
    --page-bg: #e9e6e2;
    --card-top: #2a2829;
    --card-bottom: #161617;
    --brand-blue: #2566b0;
    --accent-gold: #f2b21c;
    --card-shadow: rgba(0, 0, 0, 0.28);
  }
  * { box-sizing: border-box; margin: 0; padding: 0; }
  html, body {
    width: 1200px;
    height: 914px;
    overflow: hidden;
    background: var(--page-bg);
    font-family: "Jost", "Helvetica Neue", Arial, sans-serif;
  }
  .canvas {
    position: relative;
    width: 1200px;
    height: 914px;
  }
  .card {
    position: absolute;
    width: 640px;
    height: 366px;
    border-radius: 4px;
    background: radial-gradient(ellipse at 40% 45%, var(--card-top) 0%, var(--card-bottom) 80%);
    box-shadow: 0 14px 30px var(--card-shadow);
    overflow: hidden;
  }
  .card--back { left: 470px; top: 80px; }
  .card--front { left: 90px; top: 468px; }

  .wordmark {
    display: flex;
    align-items: center;
    gap: 12px;
    color: var(--brand-blue);
    font-weight: 300;
    font-size: 46px;
    line-height: 1.1;
    letter-spacing: 0.5px;
    white-space: nowrap;
  }
  .wordmark__dot {
    width: 16px;
    height: 16px;
    border-radius: 50%;
    background: var(--brand-blue);
    flex: none;
  }
  .tagline {
    color: var(--brand-blue);
    font-size: 17px;
    font-weight: 400;
    letter-spacing: 2px;
    text-transform: uppercase;
    white-space: nowrap;
  }

  .card--back .wordmark {
    position: absolute;
    left: 0; right: 0;
    top: 128px;
    justify-content: center;
  }
  .card--back .tagline {
    position: absolute;
    left: 0; right: 0;
    top: 190px;
    text-align: center;
  }
  .card--back .website {
    position: absolute;
    left: 0; right: 0;
    top: 222px;
    text-align: center;
    color: var(--accent-gold);
    font-size: 16px;
    font-weight: 400;
  }

  .card--front .wordmark {
    position: absolute;
    left: 34px;
    top: 36px;
  }
  .card--front .tagline {
    position: absolute;
    left: 62px;
    top: 96px;
    font-size: 14px;
  }

  .qr-space {
    position: absolute;
    left: 34px;
    bottom: 34px;
    width: 92px;
    height: 92px;
    border: 2px solid var(--accent-gold);
    border-radius: 4px;
  }

  .contact {
    position: absolute;
    right: 34px;
    bottom: 34px;
    text-align: right;
  }
  .contact__name {
    color: var(--accent-gold);
    font-size: 27px;
    font-weight: 400;
    line-height: 1.1;
  }
  .contact__role {
    color: var(--brand-blue);
    font-size: 13px;
    margin-bottom: 14px;
  }
  .contact__list { list-style: none; }
  .contact__item {
    display: flex;
    justify-content: flex-end;
    align-items: center;
    gap: 12px;
    color: var(--brand-blue);
    font-size: 16px;
    line-height: 26px;
    white-space: nowrap;
  }
  .contact__icon {
    width: 16px;
    height: 16px;
    fill: var(--accent-gold);
    flex: none;
  }
</style>
</head>
<body>
<main class="canvas">

  <section class="card card--back" aria-label="Business card back">
    <div class="wordmark"><span class="wordmark__dot"></span>Bright Canyon, LLC</div>
    <p class="tagline">Cleaner and Protectant</p>
    <p class="website">www.brightcanyoncleaner.example</p>
  </section>

  <section class="card card--front" aria-label="Business card front">
    <div class="wordmark"><span class="wordmark__dot"></span>Bright Canyon, LLC</div>
    <p class="tagline">Cleaner and Protectant</p>

    <div class="qr-space" role="img" aria-label="Space for QR code"></div>

    <div class="contact">
      <p class="contact__name">John Doe</p>
      <p class="contact__role">Managing Director</p>
      <ul class="contact__list">
        <li class="contact__item">(555) 010-2244
          <svg class="contact__icon" viewBox="0 0 16 16" aria-hidden="true"><circle cx="8" cy="5" r="3.5"/><path d="M1.5 15c0-3.6 2.9-5.5 6.5-5.5s6.5 1.9 6.5 5.5z"/></svg>
        </li>
        <li class="contact__item">info@brightcanyon.example
          <svg class="contact__icon" viewBox="0 0 16 16" aria-hidden="true"><path d="M1 3h14v10H1z M1.8 3.8 8 8.6l6.2-4.8" fill="none" stroke="var(--accent-gold)" stroke-width="1.6"/></svg>
        </li>
        <li class="contact__item">www.brightcanyoncleaner.example
          <svg class="contact__icon" viewBox="0 0 16 16" aria-hidden="true"><circle cx="8" cy="8" r="6.5" fill="none" stroke="var(--accent-gold)" stroke-width="1.6"/><path d="M1.5 8h13M8 1.5c-3 3.5-3 9.5 0 13M8 1.5c3 3.5 3 9.5 0 13" fill="none" stroke="var(--accent-gold)" stroke-width="1.2"/></svg>
        </li>
        <li class="contact__item">Bright Canyon Inc 40 Mesa Road Fairview, AZ 00000
          <svg class="contact__icon" viewBox="0 0 16 16" aria-hidden="true"><path d="M8 1.5 0.8 8h2.2v6.5h4v-4h2v4h4V8h2.2z"/></svg>
        </li>
      </ul>
    </div>
  </section>

</main>
</body>
</html>
```